Business card for dental office with laser therapy / dental facial esthetic

A simple logo which should signifies
Dentistry intraoral as primary and with extended extraoral cosmetic facial esthetic services ( regenerative skincare ) which enhance Beauty as whole .
Conservative high tech approach by using laser intraoral and extraoral limited to face and neck
Front Face :May be black background with neon blue / purplish Rim signifies laser ( ?) & abstract face profile and tooth or Apple design in one ? / see upload inspiration design
Back side : simple appointment slots with date and time / white background / black letter

Color : black/ neon blue/ purplish and gold incorporate for logo design
Final design : dental / esthetic / modern high tech and safe

Target Market(s)

Dental Patients who seeks more high end cosmetic treatment

Industry/Entity Type

Health Care

Contact Information for Business Card

Esthetic modern elegant looking
Logo and office must haves important informations

Logo Text

Brightwell Dental

Font styles to use
Script

Requirements
Must have
• Name of practice and all important informations
• Brightwell Dental
• Lan B. Okafor DMD,PC
• 38412 Brantley Court ,ste.207
• Cedar Hollow ,VA 20391
• Ph. 703-555-0187
• Fax 703-5550193
Nice to have
• More abstract
• Front : black back ground with neon blue rim (signifies laser therapy)
• Logo can also be golden gold / neon blue
• Address & Infos can be white
Should not have
• Not to busy looking

```html
<!DOCTYPE html>
<html lang="en">
<head>
<meta charset="utf-8">
<title>Brightwell Dental – Business Card</title>
<link rel="stylesheet" href="https://fonts.googleapis.com/css2?family=Exo+2:wght@400&family=Open+Sans:wght@400&display=swap">
<style>
  :root {
    --backdrop: #24272b;
    --card: #0b0b0c;
    --rim: #3fa3cf;
    --green: #8cc63f;
    --white: #ececec;
    --grey: #8d8f92;
    --rule: #2f9fc8;
  }
  html, body {
    margin: 0;
    width: 1200px;
    height: 900px;
    overflow: hidden;
    background: var(--backdrop);
  }
  .canvas {
    position: relative;
    width: 1200px;
    height: 900px;
  }
  .card {
    position: absolute;
    width: 490px;
    height: 280px;
    border-radius: 22px;
    background: var(--card);
    box-sizing: border-box;
    font-family: "Open Sans", sans-serif;
  }
  .card--front {
    left: 80px;
    top: 330px;
    border-bottom: 7px solid var(--rim);
  }
  .card--back {
    left: 630px;
    top: 110px;
    display: flex;
    align-items: center;
    justify-content: center;
  }
  .holder-name {
    position: absolute;
    left: 44px;
    top: 34px;
    margin: 0;
    font-size: 22px;
    font-weight: 400;
    color: var(--white);
  }
  .holder-title {
    position: absolute;
    left: 44px;
    top: 66px;
    margin: 0;
    font-size: 11px;
    color: var(--green);
  }
  .accent-rule {
    position: absolute;
    left: 44px;
    top: 88px;
    width: 250px;
    height: 1px;
    background: var(--rule);
  }
  .contact-list {
    position: absolute;
    left: 44px;
    top: 132px;
    margin: 0;
    padding: 0;
    list-style: none;
    font-size: 11px;
    color: var(--grey);
  }
  .contact-list li {
    display: flex;
    align-items: center;
    gap: 7px;
    margin-bottom: 6px;
  }
  .contact-list svg { width: 11px; height: 11px; }
  .practice {
    display: flex;
    align-items: center;
    gap: 10px;
    font-family: "Exo 2", sans-serif;
    color: var(--white);
  }
  .practice__dot {
    border-radius: 50%;
    background: var(--green);
  }
  .card--front .practice {
    position: absolute;
    right: 40px;
    top: 108px;
    font-size: 22px;
    color: #cfd0d1;
  }
  .card--front .practice__dot { width: 14px; height: 14px; }
  .card--back .practice { font-size: 32px; color: #cfd0d1; }
  .card--back .practice__dot { width: 20px; height: 20px; }
  .address {
    position: absolute;
    right: 40px;
    bottom: 30px;
    margin: 0;
    font-style: normal;
    text-align: right;
    font-size: 12px;
    line-height: 1.6;
    color: var(--grey);
  }
  .lockup {
    position: absolute;
    right: 80px;
    bottom: 120px;
  }
  .lockup .practice { font-size: 46px; }
  .lockup .practice__dot { width: 30px; height: 30px; }
</style>
</head>
<body>
<main class="canvas">

  <section class="card card--back" aria-label="Card back">
    <div class="practice">
      <span class="practice__dot"></span>
      <span class="practice__name">Brightwell Dental</span>
    </div>
  </section>

  <section class="card card--front" aria-label="Card front">
    <h1 class="holder-name">Lan B. Okafor</h1>
    <p class="holder-title">DMD,PC</p>
    <div class="accent-rule"></div>

    <ul class="contact-list">
      <li>
        <svg viewBox="0 0 12 12" aria-hidden="true"><path d="M3 1 L5 3.5 L4 5 Q5.5 7.5 7 8 L8.5 7 L11 9 L9.5 11 Q4 10.5 1 2.5 Z" fill="#8cc63f"/></svg>
        703-555-0187
      </li>
      <li>
        <svg viewBox="0 0 12 12" aria-hidden="true"><rect x="1" y="4" width="10" height="7" rx="1" fill="#8cc63f"/><rect x="3" y="1" width="6" height="4" fill="#8cc63f"/><rect x="3.5" y="6.5" width="5" height="1.2" fill="#0b0b0c"/></svg>
        703-5550193
      </li>
    </ul>

    <div class="practice">
      <span class="practice__dot"></span>
      <span class="practice__name">Brightwell Dental</span>
    </div>

    <address class="address">
      38412 Brantley Court ,ste.207<br>
      Cedar Hollow ,VA 20391
    </address>
  </section>

  <div class="lockup">
    <div class="practice">
      <span class="practice__dot"></span>
      <span class="practice__name">Brightwell Dental</span>
    </div>
  </div>

</main>
</body>
</html>
```